Need a sleek, professional business card design for a Web Development business

I need a unique business card designed for a web development company. It is also the parent company for any ventures I do, such as my ClipHarbor channel, startup ideas I have, etc. I am the single member of "Copper Lantern Sites LLC." I will attach my basic logo here, so you will see the current color scheme and have the asset available. Thank you!

Target Market(s)

Startups, SMB's, Professionals

Industry/Entity Type

Business

Font styles to use
Other font styles liked:
• Lovello for headings is what I use, but not necessary.

Colors

Designer to choose colors to be used in the design.

Requirements
Nice to have
• Sleek is the word. Professional, modern, dark.
Should not have
• Any work from someone else's design. Lacking originality.

```html
<!DOCTYPE html>
<html lang="en">
<head>
<meta charset="utf-8">
<title>Copper Lantern Sites LLC – Business Card</title>
<link rel="stylesheet" href="https://fonts.googleapis.com/css2?family=Noto+Sans:wght@400;600;700&display=swap">
<style>
  :root {
    --backdrop: #3a312d;
    --card: #1b1b1b;
    --card-edge: #262626;
    --orange: #f5a04e;
    --coral: #f0667a;
    --muted: #8a8380;
  }
  * { box-sizing: border-box; margin: 0; padding: 0; }
  html, body {
    width: 1200px;
    height: 715px;
    overflow: hidden;
    background: var(--backdrop);
    font-family: "Noto Sans", sans-serif;
  }
  .stage {
    position: relative;
    width: 1200px;
    height: 715px;
  }
  .card {
    position: absolute;
    top: 207px;
    width: 520px;
    height: 300px;
    background: var(--card);
    border: 1px solid var(--card-edge);
    border-radius: 4px;
    box-shadow: 0 10px 30px rgba(0, 0, 0, 0.45);
  }
  .card--front { left: 50px; }
  .card--back { left: 630px; }

  /* Front */
  .brand {
    position: absolute;
    inset: 0;
    display: flex;
    flex-direction: column;
    align-items: center;
    justify-content: center;
    gap: 22px;
  }
  .brand__mark {
    width: 96px;
    height: 96px;
    border-radius: 18px;
    background: var(--orange);
  }
  .brand__name {
    color: var(--orange);
    font-weight: 700;
    font-size: 17px;
    letter-spacing: 0.3px;
  }

  /* Back */
  .holder {
    position: absolute;
    left: 34px;
    top: 30px;
  }
  .holder__name {
    color: var(--coral);
    font-weight: 700;
    font-size: 17px;
    letter-spacing: 0.5px;
  }
  .holder__title {
    color: var(--muted);
    font-size: 10px;
    margin-top: 2px;
  }
  .contacts {
    position: absolute;
    left: 34px;
    bottom: 36px;
    list-style: none;
    display: flex;
    flex-direction: column;
    gap: 7px;
  }
  .contacts__item {
    display: flex;
    align-items: center;
    gap: 10px;
    color: var(--orange);
    font-size: 13px;
    letter-spacing: 0.4px;
  }
  .contacts__icon {
    width: 13px;
    height: 13px;
    flex: none;
    color: var(--coral);
  }
  .signoff {
    position: absolute;
    right: 30px;
    bottom: 28px;
    display: flex;
    align-items: center;
    gap: 10px;
  }
  .signoff__mark {
    width: 70px;
    height: 70px;
    border-radius: 14px;
    background: var(--orange);
  }
</style>
</head>
<body>
<main class="stage">
  <section class="card card--front" aria-label="Card front">
    <div class="brand">
      <div class="brand__mark" aria-hidden="true"></div>
      <p class="brand__name">Copper Lantern Sites LLC</p>
    </div>
  </section>

  <section class="card card--back" aria-label="Card back">
    <header class="holder">
      <h1 class="holder__name">Your Name</h1>
      <p class="holder__title">Title</p>
    </header>

    <ul class="contacts">
      <li class="contacts__item">
        <svg class="contacts__icon" viewBox="0 0 16 16" aria-hidden="true">
          <circle cx="8" cy="8" r="7" fill="none" stroke="currentColor" stroke-width="1.5"/>
          <path d="M5.5 4.5l1.5 0 .7 1.8-.9.8a5 5 0 0 0 2.1 2.1l.8-.9 1.8.7v1.5c-3.5.3-6.3-2.5-6-6z" fill="currentColor"/>
        </svg>
        <span>0455 210 384</span>
      </li>
      <li class="contacts__item">
        <svg class="contacts__icon" viewBox="0 0 16 16" aria-hidden="true">
          <rect x="1" y="3" width="14" height="10" rx="1" fill="currentColor"/>
          <path d="M1.5 3.8L8 9l6.5-5.2" fill="none" stroke="var(--card)" stroke-width="1.3"/>
        </svg>
        <span>info@copperlanternsites.com</span>
      </li>
      <li class="contacts__item">
        <svg class="contacts__icon" viewBox="0 0 16 16" aria-hidden="true">
          <g fill="none" stroke="currentColor" stroke-width="1.2">
            <circle cx="8" cy="8" r="6.5"/>
            <ellipse cx="8" cy="8" rx="3" ry="6.5"/>
            <path d="M1.5 8h13M2.5 4.7h11M2.5 11.3h11"/>
          </g>
        </svg>
        <span>www.copperlanternsites.com</span>
      </li>
      <li class="contacts__item">
        <svg class="contacts__icon" viewBox="0 0 16 16" aria-hidden="true">
          <path d="M8 1a5 5 0 0 0-5 5c0 3.8 5 9 5 9s5-5.2 5-9a5 5 0 0 0-5-5z" fill="currentColor"/>
          <circle cx="8" cy="6" r="1.9" fill="var(--card)"/>
        </svg>
        <span>Your Complete Address is here</span>
      </li>
    </ul>

    <div class="signoff">
      <div class="signoff__mark" aria-hidden="true"></div>
    </div>
  </section>
</main>
</body>
</html>
```